Serenqora: a Holistic Healing Company
Serenqora: Unlocking the Strengths for Balance Inside Each of Us
TO ALL DESIGNERS:
PLEASE BE SURE TO CHANGE THE WORD "PRESIDENT' TO "FOUNDER" (DO NOT ADD QUOTES)
ALSO, PLEASE ADD THE CELL NUMBER AS WELL AS THE TOLL FREE NUMBER.
THANK YOU!
PLEASE PROVIDE DESIGNS FOR LETTER HEADS AND ENVELOPES TOO. THANKYOU
THIS CONTEST IS FOR BOTH BUSINESS CARD DESIGN AND
STATIONARY DESIGN USING THE SERENQORA LOGO.

```html
<!DOCTYPE html>
<html lang="en">
<head>
<meta charset="utf-8">
<title>Serenqora Stationery</title>
<link href="https://fonts.googleapis.com/css2?family=Montserrat:wght@400;600&display=swap" rel="stylesheet">
<style>
:root{
  --blue:#1f8ad8;
  --blue-deep:#0d5ea8;
  --ink:#111417;
  --grey:#6b7178;
  --paper:#ffffff;
  --stage:#ffffff;
  --shadow:rgba(0,0,0,.28);
}
*{box-sizing:border-box;margin:0;padding:0}
html,body{width:1200px;height:348px;overflow:hidden;background:var(--stage);font-family:"Montserrat",sans-serif;color:var(--ink)}
.canvas{position:relative;width:1200px;height:348px}
.sheet{position:absolute;background:var(--paper);box-shadow:1px 2px 5px var(--shadow);overflow:hidden}
.swoosh{position:absolute;left:0;top:0;width:100%;height:100%}
.brand{position:absolute;display:flex;align-items:center;gap:3px}
.brand-dot{width:7px;height:7px;border-radius:50%;background:var(--blue)}
.brand-name{font-weight:600;font-size:7px;letter-spacing:1.4px;color:var(--ink)}
.brand.on-dark .brand-name{color:var(--paper)}
.brand-tag{position:absolute;font-size:3.4px;color:var(--grey);letter-spacing:.2px}
.small{position:absolute;font-size:3.6px;line-height:5px;color:var(--grey)}
.on-dark-text{color:#d9dde2}
.envelope{width:258px;height:113px}
.envelope-front{top:24px}
.envelope-back{top:162px}
.flap{position:absolute;left:0;top:0;width:100%;height:100%}
.letterhead{top:19px;width:162px;height:312px}
.card{width:89px;height:58px}
.card.dark{background:var(--ink)}
.brand.center{left:50%;top:50%;transform:translate(-50%,-50%)}
</style>
</head>
<body>
<main class="canvas">

  <!-- Set one -->
  <section class="sheet envelope envelope-front" style="left:29px">
    <svg class="swoosh" viewBox="0 0 258 113" preserveAspectRatio="none" aria-hidden="true">
      <path d="M0 0 H10 Q32 56 12 113 H0 Z" fill="var(--ink)"/>
      <path d="M10 0 Q32 56 12 113" fill="none" stroke="var(--blue)" stroke-width="2"/>
      <path d="M16 0 Q38 56 18 113" fill="none" stroke="var(--blue)" stroke-width=".8"/>
    </svg>
    <div class="brand" style="left:36px;top:10px"><span class="brand-dot"></span><span class="brand-name">SERENQORA</span></div>
    <div class="brand-tag" style="left:46px;top:21px">a Holistic Healing Company</div>
    <div class="small" style="left:46px;top:28px">12 Willow Lane<br>Asheville, NC 28801</div>
  </section>
  <section class="sheet envelope envelope-back" style="left:29px">
    <svg class="flap" viewBox="0 0 258 113" preserveAspectRatio="none" aria-hidden="true">
      <path d="M0 0 L129 52 L258 0" fill="none" stroke="#c9ccd0" stroke-width=".8"/>
      <path d="M0 113 L110 58 M258 113 L148 58" fill="none" stroke="#dcdfe2" stroke-width=".8"/>
    </svg>
    <div class="brand" style="left:50%;top:48px;transform:translateX(-50%)"><span class="brand-dot"></span><span class="brand-name">SERENQORA</span></div>
  </section>

  <section class="sheet letterhead" style="left:312px">
    <svg class="swoosh" viewBox="0 0 162 312" preserveAspectRatio="none" aria-hidden="true">
      <path d="M0 20 Q30 160 6 312 H0 Z" fill="var(--ink)"/>
      <path d="M4 0 Q38 160 12 312" fill="none" stroke="var(--blue)" stroke-width="2.4"/>
      <path d="M10 0 Q44 160 18 312" fill="none" stroke="var(--blue-deep)" stroke-width=".8"/>
    </svg>
    <div class="brand" style="left:30px;top:12px"><span class="brand-dot"></span><span class="brand-name">SERENQORA</span></div>
    <div class="brand-tag" style="left:40px;top:23px">a Holistic Healing Company</div>
    <div class="small" style="left:40px;top:32px">12 Willow Lane<br>Asheville, NC 28801<br>800.555.0142</div>
  </section>

  <section class="sheet card dark" style="left:492px;top:62px">
    <svg class="swoosh" viewBox="0 0 89 58" preserveAspectRatio="none" aria-hidden="true">
      <path d="M0 58 Q40 40 89 46" fill="none" stroke="var(--blue)" stroke-width="1.2"/>
    </svg>
    <div class="small on-dark-text" style="left:7px;top:7px">Mara Lindqvist<br>Founder<br>Cell 828.555.0193<br>Toll Free 800.555.0142<br>mara@serenqora.com</div>
  </section>
  <section class="sheet card dark" style="left:492px;top:132px">
    <div class="brand center on-dark"><span class="brand-dot"></span><span class="brand-name">SERENQORA</span></div>
  </section>

  <!-- Set two -->
  <section class="sheet envelope envelope-front" style="left:619px">
    <svg class="swoosh" viewBox="0 0 258 113" preserveAspectRatio="none" aria-hidden="true">
      <path d="M4 0 Q30 56 8 113" fill="none" stroke="var(--ink)" stroke-width="1.6"/>
      <path d="M10 0 Q36 56 14 113" fill="none" stroke="var(--blue)" stroke-width="2"/>
      <path d="M16 0 Q42 56 20 113" fill="none" stroke="var(--blue)" stroke-width=".7"/>
    </svg>
    <div class="brand" style="left:36px;top:10px"><span class="brand-dot"></span><span class="brand-name">SERENQORA</span></div>
    <div class="brand-tag" style="left:46px;top:21px">a Holistic Healing Company</div>
    <div class="small" style="left:46px;top:28px">12 Willow Lane<br>Asheville, NC 28801</div>
  </section>
  <section class="sheet envelope envelope-back" style="left:619px">
    <svg class="flap" viewBox="0 0 258 113" preserveAspectRatio="none" aria-hidden="true">
      <path d="M0 0 L129 52 L258 0" fill="none" stroke="#c9ccd0" stroke-width=".8"/>
      <path d="M0 113 L110 58 M258 113 L148 58" fill="none" stroke="#dcdfe2" stroke-width=".8"/>
    </svg>
    <div class="brand" style="left:50%;top:48px;transform:translateX(-50%)"><span class="brand-dot"></span><span class="brand-name">SERENQORA</span></div>
  </section>

  <section class="sheet letterhead" style="left:895px">
    <svg class="swoosh" viewBox="0 0 162 312" preserveAspectRatio="none" aria-hidden="true">
      <path d="M4 0 Q36 160 8 312" fill="none" stroke="var(--ink)" stroke-width="1.8"/>
      <path d="M10 0 Q42 160 14 312" fill="none" stroke="var(--blue)" stroke-width="2.4"/>
      <path d="M16 0 Q48 160 20 312" fill="none" stroke="var(--blue-deep)" stroke-width=".8"/>
    </svg>
    <div class="brand" style="left:30px;top:12px"><span class="brand-dot"></span><span class="brand-name">SERENQORA</span></div>
    <div class="brand-tag" style="left:40px;top:23px">a Holistic Healing Company</div>
    <div class="small" style="left:40px;top:32px">12 Willow Lane<br>Asheville, NC 28801<br>800.555.0142</div>
  </section>

  <section class="sheet card" style="left:1068px;top:96px">
    <svg class="swoosh" viewBox="0 0 89 58" preserveAspectRatio="none" aria-hidden="true">
      <path d="M0 58 Q40 40 89 46" fill="none" stroke="var(--blue)" stroke-width="1.2"/>
    </svg>
    <div class="brand" style="left:6px;top:6px"><span class="brand-dot"></span><span class="brand-name">SERENQORA</span></div>
    <div class="small" style="left:8px;top:18px">Mara Lindqvist, Founder<br>Cell 828.555.0193<br>Toll Free 800.555.0142<br>mara@serenqora.com</div>
  </section>
  <section class="sheet card" style="left:1080px;top:142px">
    <div class="brand center"><span class="brand-dot"></span><span class="brand-name">SERENQORA</span></div>
  </section>

</main>
</body>
</html>
```